Brookside Grocer

Hope all is well!

Wanted to make business cards for my father. His name is Faisal Qureshi and owns convenience stores. I have attached logo :)

He does not want any title just simple name and phone. An email would be nice as well.

Faisal Qureshi
Cell: 413-585-2046
Store: 413-719-4820

Brooksidegrocer512@fernpost.com

The design and style is totally up to you :) The colors we were looking for were the same as logo :)

```html
<!DOCTYPE html>
<html lang="en">
<head>
<meta charset="utf-8">
<title>Brookside Grocer — Business Cards</title>
<link rel="stylesheet" href="https://fonts.googleapis.com/css2?family=Tinos:wght@700&family=Questrial&display=swap">
<style>
  :root {
    --backdrop: #d1d2d4;
    --card: #ffffff;
    --navy: #233a7c;
    --red: #ee3a3d;
  }
  * { margin: 0; padding: 0; box-sizing: border-box; }
  html, body {
    width: 900px;
    height: 1200px;
    overflow: hidden;
    background: var(--backdrop);
  }
  .card {
    position: absolute;
    left: 133px;
    width: 633px;
    height: 364px;
    background: var(--card);
  }
  .card--front { top: 210px; }
  .card--back { top: 624px; }

  .brand-name {
    position: absolute;
    left: 0;
    right: 0;
    text-align: center;
    font-family: "Tinos", "Times New Roman", serif;
    font-weight: 700;
    color: var(--navy);
    white-space: nowrap;
  }
  .card--front .brand-name {
    top: 152px;
    font-size: 44px;
    line-height: 56px;
    letter-spacing: 0.5px;
  }
  .card--back .brand-name {
    top: 60px;
    font-size: 32px;
    line-height: 40px;
    letter-spacing: 0.3px;
  }

  .contact {
    position: absolute;
    left: 187px;
    top: 182px;
    width: 264px;
  }
  .contact__name {
    font-family: "Tinos", "Times New Roman", serif;
    font-weight: 700;
    font-size: 27px;
    line-height: 30px;
    color: var(--navy);
    letter-spacing: 0.6px;
    white-space: nowrap;
  }
  .contact__rule {
    display: block;
    margin-top: 12px;
    width: 264px;
    height: 14px;
  }
  .contact__list {
    list-style: none;
    margin-top: 12px;
    font-family: "Questrial", "Helvetica", sans-serif;
    color: var(--navy);
  }
  .contact__item {
    white-space: nowrap;
    height: 26px;
    line-height: 26px;
  }
  .contact__item--phone {
    font-size: 20px;
    letter-spacing: 3px;
  }
  .contact__item--email {
    font-size: 16px;
    letter-spacing: 0;
  }
  .contact__label { color: var(--red); letter-spacing: 0; margin-right: 2px; }
</style>
</head>
<body>
  <section class="card card--front" aria-label="Card front">
    <div class="brand-name">BROOKSIDE GROCER</div>
  </section>

  <section class="card card--back" aria-label="Card back">
    <div class="brand-name">BROOKSIDE GROCER</div>

    <div class="contact">
      <h1 class="contact__name">FAISAL QURESHI</h1>
      <svg class="contact__rule" viewBox="0 0 264 14" aria-hidden="true">
        <rect x="0" y="0" width="264" height="3" fill="var(--red)"/>
        <rect x="0" y="5.5" width="264" height="3" fill="var(--red)"/>
        <rect x="0" y="11" width="264" height="3" fill="var(--red)"/>
      </svg>
      <ul class="contact__list">
        <li class="contact__item contact__item--phone"><span class="contact__label">C:</span>413-585-2046</li>
        <li class="contact__item contact__item--phone"><span class="contact__label">S:</span>413-719-4820</li>
        <li class="contact__item contact__item--email"><span class="contact__label">E:</span>Brooksidegrocer512@fernpost.com</li>
      </ul>
    </div>
  </section>
</body>
</html>
```